eMail HTML Marketing Template

I need an HTML e-mail marketing template design based off our current website theme (www.tindleport.com). If you need anymore info or have questions please let me know and I will get back to you ASAP.

Goal: A monthly newsletter template for email marketing. Please use lorem ipsum for content filler. If you need to purchase images for the design please let me know and the price to do so.

Thanks.

***URGENT***
If anyone can provide a well designed mockup by 4:00PM EST today (2/6/13) I will award up to two participation prizes of $20 each to each submitter.

Goal: A monthly newsletter template for email marketing.  Please use lorem ipsum for content filler. If you need to purchase images for the design please let me know and the price to do so.

Thanks.

***URGENT***

Marketing

```html
<!DOCTYPE html>
<html lang="en">
<head>
<meta charset="utf-8">
<title>Tindleport Newsletter – February 2013</title>
<link rel="stylesheet" href="https://fonts.googleapis.com/css2?family=Open+Sans:wght@400;600&family=Cabin+Condensed:wght@400&display=swap">
<style>
  :root {
    --brand-green: #5aa800;
    --brand-blue: #2b4c94;
    --ink: #111111;
    --paper: #ffffff;
    --rule: #d6d6d6;
    --footer-black: #000000;
    --heading-font: "Open Sans", Arial, sans-serif;
    --body-font: "Cabin Condensed", "Trebuchet MS", sans-serif;
  }
  * { margin: 0; padding: 0; box-sizing: border-box; }
  html, body { width: 1200px; height: 2400px; overflow: hidden; background: var(--paper); }
  .newsletter { position: relative; width: 1200px; height: 2400px; color: var(--ink); font-family: var(--body-font); }
  .abs { position: absolute; }

  .hero-photo { left: 80px; top: 0; width: 1040px; height: 694px;
    background: linear-gradient(120deg, #e9eef0 0%, #c9d3d6 35%, #f3e6e0 55%, #b7c9cf 80%, #8fa7b3 100%); }
  .logo-box { left: 0; top: 80px; width: 506px; height: 134px; background: var(--footer-black);
    display: flex; align-items: center; padding-left: 90px; gap: 18px; }
  .logo-dot { width: 40px; height: 40px; border-radius: 50%; background: var(--brand-green); }
  .logo-name { font-family: var(--heading-font); font-weight: 600; font-size: 46px; color: var(--brand-green); }
  .issue-date { left: 860px; top: 80px; width: 340px; height: 104px; background: var(--brand-blue);
    color: var(--paper); font-family: var(--heading-font); font-size: 28px; line-height: 104px; padding-left: 28px; }
  .hero-tag { left: 546px; top: 522px; width: 654px; height: 172px; background: var(--brand-green);
    color: var(--paper); font-family: var(--heading-font); padding: 28px 0 0 38px; }
  .hero-tag .big { font-size: 68px; line-height: 68px; }
  .hero-tag .sub { font-size: 35px; line-height: 52px; }

  .intro { left: 76px; top: 750px; width: 720px; }
  .intro p:first-child { font-size: 24px; line-height: 36px; }
  .intro p:last-child { font-size: 27px; line-height: 37px; margin-top: 22px; }
  .freebie-photo { left: 828px; top: 770px; width: 372px; height: 216px;
    background: linear-gradient(90deg, #f06aa0 0%, #f7b733 30%, #39b6d8 55%, #e0336e 80%, #f28a3c 100%); }
  .freebie-button { left: 812px; top: 986px; width: 388px; height: 100px; background: var(--brand-blue);
    color: var(--paper); font-family: var(--heading-font); font-size: 27px; text-align: center; line-height: 100px; }

  .rule { left: 60px; width: 1064px; height: 2px; background: var(--rule); }

  .featured-photo { left: 0; top: 1166px; width: 450px; height: 302px;
    background: linear-gradient(135deg, #ffffff 0%, #f6f1e6 50%, #f2e3c8 70%, #e81818 100%); }
  .section-title { font-family: var(--heading-font); font-size: 36px; line-height: 44px; }
  .section-copy { font-size: 20px; line-height: 32px; }
  .featured-text { left: 414px; top: 1222px; width: 690px; }
  .featured-text .section-copy { margin-top: 18px; }
  .discount-text { left: 82px; top: 1546px; width: 470px; }
  .discount-text .section-copy { margin-top: 18px; }
  .discount-photo { left: 608px; top: 1496px; width: 412px; height: 262px;
    background: linear-gradient(120deg, #e4ea3a 0%, #f06a1c 35%, #9b4fd8 65%, #3f8fd8 100%); }

  .beta-badge { left: 84px; top: 1814px; width: 300px; height: 300px; }
  .beta-badge-label { left: 84px; top: 1894px; width: 300px; text-align: center; color: var(--paper);
    font-family: var(--heading-font); }
  .beta-badge-label .small { font-size: 34px; line-height: 40px; }
  .beta-badge-label .large { font-size: 44px; line-height: 52px; }
  .beta-text { left: 410px; top: 1830px; width: 716px; }

  .social-band { left: 0; top: 2160px; width: 1200px; height: 80px; background: var(--brand-blue); }
  .social-band svg { position: absolute; left: 480px; top: 10px; }
  .legal { left: 0; top: 2240px; width: 1200px; height: 160px; background: var(--footer-black);
    color: var(--paper); text-align: center; font-family: var(--heading-font); font-size: 22px; line-height: 28px; padding-top: 10px; }
</style>
</head>
<body>
<div class="newsletter">
  <div class="abs hero-photo" role="img" aria-label="Photo of a smiling woman in a shopping mall holding shopping bags and looking at her phone"></div>
  <div class="abs logo-box"><span class="logo-dot"></span><span class="logo-name">Tindleport</span></div>
  <div class="abs issue-date">FEBRUARY 2013</div>
  <div class="abs hero-tag"><div class="big">GRAB</div><div class="sub">YOUR FREE CUSTOMERS TODAY!</div></div>

  <div class="abs intro">
    <p>This is Tindleport's gift to you as we launch our business. Using our unique social media platform, we will present your business to millions of consumers as we launch.</p>
    <p>Simply use and activate a Discount Deal or place items to our MarketPlace to take advantage of this deal. Tindleport will deliver 1...</p>
  </div>
  <div class="abs freebie-photo" role="img" aria-label="Photo of colourful shopping bags"></div>
  <div class="abs freebie-button">VIEW THIS FREEBIE!</div>

  <div class="abs rule" style="top:1128px"></div>

  <div class="abs featured-photo" role="img" aria-label="Photo of a hand holding a clothes hanger with a red sale tag"></div>
  <div class="abs featured-text">
    <h2 class="section-title">FEATURED DEALS</h2>
    <p class="section-copy">Lorem Ipsum has been the industry's standard dummy text ever since the 1500s, when an unknown printeley of type and scrambled it to make a type specimen book.</p>
  </div>

  <div class="abs rule" style="top:1468px"></div>

  <div class="abs discount-text">
    <h2 class="section-title">DISCUNT DEALS</h2>
    <p class="section-copy">Lorem Ipsum has been the industry's standard dummy text ever since the 1500s, when an unknown printeley of type and scrambled it to make a type specimen book.</p>
  </div>
  <div class="abs discount-photo" role="img" aria-label="Photo of a laughing woman in sunglasses holding colourful shopping bags"></div>

  <div class="abs rule" style="top:1788px"></div>

  <svg class="abs beta-badge" viewBox="0 0 300 300" aria-hidden="true">
    <polygon fill="var(--brand-green)" points="298,150 272.5,169.3 290.7,195.7 260.5,206.3 269.7,237 237.7,237.7 237,269.7 206.3,260.5 195.7,290.7 169.3,272.5 150,298 130.7,272.5 104.3,290.7 93.7,260.5 63,269.7 62.3,237.7 30.3,237 39.5,206.3 9.3,195.7 27.5,169.3 2,150 27.5,130.7 9.3,104.3 39.5,93.7 30.3,63 62.3,62.3 63,30.3 93.7,39.5 104.3,9.3 130.7,27.5 150,2 169.3,27.5 195.7,9.3 206.3,39.5 237,30.3 237.7,62.3 269.7,63 260.5,93.7 290.7,104.3 272.5,130.7"/>
  </svg>
  <div class="abs beta-badge-label">
    <div class="small">BETA TEST</div>
    <div class="large">DISCOUNT</div>
    <div class="large">DEAL</div>
  </div>
  <p class="abs beta-text section-copy">Lorem Ipsum has been the industry's standard dummy text ever since the 1500s, when an unknown printeley of type and scrambled it to make a type specimen book. Lorem Ipsum has been the industry's standard dummy text ever since the 1500s, when an unknown printeley of type and scrambled it to make a type specimen book. Lorem Ipsum has been the industry's standard dummy text ever since the 1500s, when an unknown printeley of type and scrambled it to make a type specimen book.</p>

  <div class="abs social-band">
    <svg width="240" height="60" viewBox="0 0 240 60" aria-hidden="true">
      <circle cx="34" cy="30" r="23" fill="none" stroke="#ffffff" stroke-width="4"/>
      <circle cx="104" cy="30" r="23" fill="none" stroke="#ffffff" stroke-width="4"/>
      <circle cx="172" cy="30" r="23" fill="none" stroke="#ffffff" stroke-width="4"/>
    </svg>
  </div>
  <div class="abs legal">
    <p>You are receiving this email as a part of your company's program.</p>
    <p>Copyright © 2012 Tindleport All rights reserved.</p>
  </div>
</div>
</body>
</html>
```